Brochure Design - Non-Profit Fundraising Stream

We are a non-profit organization that is developing a fundraising project through the donation of life insurance policies. We have three brochures in each English and French that we developed for a sister organization that we want to reintegrate with our Foundation, keeping the same copy text just changing the logos, colors and make it overall more visually appealing. The foundation is called the 'Varnek-Holt Syndrome Foundation Canada'.
The original files in .docx format are attached as is the full logo and two symbol files. The deliverables would be six documents in total (InDesign or .docx), each brochure in English and French. The color hex codes are:
red: #7b2850
dark blue: #2c79a7
pale blue: #78b2e2

```html
<!DOCTYPE html>
<html lang="fr">
<head>
<meta charset="utf-8">
<title>Varnek-Holt Syndrome Foundation Canada – Don de police d'assurance-vie</title>
<link rel="stylesheet" href="https://fonts.googleapis.com/css2?family=Crimson+Text:wght@400;600&family=Playfair+Display:wght@700&display=swap">
<style>
  :root {
    --red: #7b2850;
    --dark-blue: #2c79a7;
    --pale-blue: #78b2e2;
    --soft-blue: #b9d6f0;
    --ink: #1f1f24;
    --paper: #ffffff;
  }
  * { margin: 0; padding: 0; box-sizing: border-box; }
  html, body { width: 849px; height: 1200px; overflow: hidden; background: var(--paper); }
  .brochure {
    position: relative;
    width: 849px;
    height: 1200px;
    overflow: hidden;
    background: var(--paper);
    font-family: "Crimson Text", Georgia, serif;
    color: var(--ink);
  }
  .deco { position: absolute; inset: 0; width: 849px; height: 1200px; }

  .brand {
    position: absolute;
    left: 42px;
    top: 24px;
    display: flex;
    align-items: center;
    gap: 14px;
  }
  .brand-dot {
    width: 46px; height: 46px; border-radius: 50%;
    background: var(--dark-blue);
  }
  .brand-name {
    font-family: "Crimson Text", Georgia, serif;
    font-weight: 600;
    font-size: 25px;
    line-height: 1.1;
    color: var(--dark-blue);
    width: 270px;
  }

  .section-title {
    position: absolute;
    left: 127px;
    font-family: "Playfair Display", Georgia, serif;
    font-weight: 700;
    font-size: 30px;
    color: var(--red);
  }
  .title-autonomy { top: 95px; }
  .title-process { top: 356px; left: 270px; }
  .title-disclosure { top: 592px; }

  .bullets {
    position: absolute;
    left: 150px;
    width: 590px;
    list-style: disc;
    font-size: 20px;
    line-height: 1.22;
  }
  .bullets li { padding-left: 6px; margin-bottom: 2px; }
  .bullets li::marker { font-size: 18px; }
  .bullets-autonomy { top: 150px; }
  .bullets-disclosure { top: 648px; }

  .process { position: absolute; left: 0; top: 395px; width: 849px; height: 185px; }
  .step {
    position: absolute;
    border-radius: 50%;
    display: flex;
    align-items: center;
    justify-content: center;
    text-align: center;
    font-size: 10.5px;
    line-height: 1.2;
    padding: 14px;
  }
  .step-pale { background: var(--pale-blue); color: var(--paper); }
  .step-dark { background: var(--dark-blue); color: var(--paper); }

  .contact-bar {
    position: absolute;
    left: 113px;
    top: 948px;
    width: 736px;
    height: 62px;
    background: var(--red);
    color: var(--paper);
    display: flex;
    align-items: center;
    justify-content: center;
    font-size: 21px;
    font-weight: 600;
    letter-spacing: 0.2px;
  }
</style>
</head>
<body>
<div class="brochure">
  <svg class="deco" viewBox="0 0 849 1200" aria-hidden="true">
    <circle cx="760" cy="80" r="130" fill="var(--soft-blue)" opacity="0.55"/>
    <circle cx="12" cy="262" r="68" fill="var(--soft-blue)" opacity="0.6"/>
    <circle cx="820" cy="590" r="115" fill="var(--soft-blue)" opacity="0.5"/>
    <circle cx="60" cy="1110" r="120" fill="var(--soft-blue)" opacity="0.5"/>
    <circle cx="470" cy="1180" r="40" fill="var(--soft-blue)" opacity="0.4"/>
  </svg>

  <header class="brand">
    <span class="brand-dot"></span>
    <span class="brand-name">Varnek-Holt Syndrome Foundation Canada</span>
  </header>

  <h2 class="section-title title-autonomy">Maintenez votre autonomie financière</h2>
  <ul class="bullets bullets-autonomy">
    <li>Financement de dépenses liées à la retraite ou à des soins de longue durée grâce à la réduction de l'impôt à la suite du reçu fiscal</li>
    <li>Réallocation des bénéfices vers des rentes ou des actifs produisant des revenus</li>
    <li>Réduction ou paiement de dettes en suspens</li>
  </ul>

  <h2 class="section-title title-process">Processus de don</h2>
  <div class="process">
    <svg class="deco" viewBox="0 0 849 185" style="height:185px" aria-hidden="true">
      <polyline points="112,95 255,58 398,118 545,58 685,118" fill="none" stroke="var(--dark-blue)" stroke-width="2"/>
    </svg>
    <div class="step step-pale" style="left:55px;top:40px;width:115px;height:110px;">Compléter le formulaire de demande de don de police</div>
    <div class="step step-dark" style="left:190px;top:5px;width:130px;height:105px;">Fournir l'information médicale</div>
    <div class="step step-pale" style="left:340px;top:65px;width:116px;height:105px;">Signer les documents de transfert de propriété</div>
    <div class="step step-dark" style="left:480px;top:5px;width:130px;height:105px;">Convertir le reçu fiscal en argent</div>
    <div class="step step-pale" style="left:625px;top:65px;width:120px;height:105px;">Recevoir le reçu fiscal en argent dans vos poches</div>
  </div>

  <h2 class="section-title title-disclosure">Divulgation</h2>
  <ul class="bullets bullets-disclosure">
    <li>Les titulaires de polices doivent demander leur propre avis professionnel, fiscal, juridique et financier.</li>
    <li>Le produit est traité comme une disposition pour fins d'impôt et est imposé sur l'excédent par rapport au coût rajusté, ce qui comprend toutes les primes payées sur le contrat, moins le coût net de l'assurance pure.</li>
    <li>Le changement de propriété d'une police peut limiter la capacité de l'assuré à souscrire à une éventuelle assurance en raison des limites de la couverture que les assureurs délivreront.</li>
    <li>Les donateurs de polices d'assurance-vie devront donner leur consentement pour permettre l'accès à leurs dossiers médicaux pour fins d'évaluation de la police d'assurance-vie. Ces renseignements demeureront confidentiels.</li>
  </ul>

  <footer class="contact-bar">Contactez-nous 1(800) 555-0147 | varnekholtcanada.org</footer>
</div>
</body>
</html>
```